Letterhead to Introduce a 'Sister' Company.

What I am needing is a design for a letter head to introduce our current customers base of (KT Alarm) customers to our new service, 'Kestrel Tide Solar Brokers'

```html
<!DOCTYPE html>
<html lang="en">
<head>
<meta charset="utf-8">
<title>Kestrel Tide Solar Brokers – Letterhead</title>
<link rel="stylesheet" href="https://fonts.googleapis.com/css2?family=Arimo:wght@400;700&display=swap">
<style>
  :root {
    --backdrop: #9e9e9e;
    --paper: #ffffff;
    --navy: #0f4a80;
    --amber: #f7a01e;
    --ink-light: #ffffff;
  }
  * { margin: 0; padding: 0; box-sizing: border-box; }
  html, body {
    width: 1200px;
    height: 1200px;
    overflow: hidden;
    background: var(--backdrop);
    font-family: "Arimo", Arial, sans-serif;
  }
  .letterhead {
    position: absolute;
    left: 192px;
    top: 102px;
    width: 816px;
    height: 996px;
    background: var(--paper);
    overflow: hidden;
  }
  .header-shapes {
    position: absolute;
    left: 0;
    top: 0;
    width: 816px;
    height: 130px;
  }
  .brand {
    position: absolute;
    left: 64px;
    top: 26px;
    width: 262px;
    display: flex;
    flex-direction: column;
    align-items: center;
    color: var(--navy);
    font-weight: 700;
  }
  .brand-dot {
    width: 46px;
    height: 46px;
    border-radius: 50%;
    background: var(--amber);
    margin-bottom: 10px;
  }
  .brand-name {
    font-size: 25px;
    letter-spacing: 1.5px;
    line-height: 1;
    text-transform: uppercase;
  }
  .brand-tag {
    margin-top: 5px;
    font-size: 11px;
    letter-spacing: 2.5px;
    line-height: 1;
    text-transform: uppercase;
  }
  .contact-list {
    position: absolute;
    left: 573px;
    top: 28px;
    list-style: none;
    color: var(--ink-light);
    font-size: 15.5px;
    line-height: 19.5px;
  }
  .contact-list li {
    display: flex;
    align-items: center;
    gap: 6px;
  }
  .contact-list svg {
    width: 14px;
    height: 14px;
    flex: none;
    fill: var(--ink-light);
  }
</style>
</head>
<body>
  <main class="letterhead">
    <svg class="header-shapes" viewBox="0 0 816 130" aria-hidden="true">
      <rect x="0" y="0" width="816" height="13" fill="var(--navy)"/>
      <polygon points="386,0 816,0 816,98 446,98" fill="var(--navy)"/>
      <polygon points="451,107 816,107 816,128 469,128" fill="var(--amber)"/>
    </svg>

    <div class="brand">
      <span class="brand-dot"></span>
      <span class="brand-name">Kestrel Tide</span>
      <span class="brand-tag">Solar Brokers</span>
    </div>

    <ul class="contact-list">
      <li>
        <svg viewBox="0 0 16 16"><path d="M1 3h14v10H1z M1 3l7 6 7-6" fill="none" stroke="#fff" stroke-width="1.6"/><path d="M1.5 3.5h13L8 8.8z"/></svg>
        hello@kestreltidesolar.com
      </li>
      <li>
        <svg viewBox="0 0 16 16"><path d="M3.6 1.2l2.3 2.6-1.3 1.9c.9 2 2.5 3.6 4.5 4.6l1.9-1.3 2.6 2.3-1.4 2.4C7 13.4 2.5 8.9 1.1 2.6z"/></svg>
        5550-142-387
      </li>
      <li>
        <svg viewBox="0 0 16 16"><circle cx="8" cy="8" r="6.6" fill="none" stroke="#fff" stroke-width="1.6"/><path d="M1.5 8h13M8 1.4c-3 3.5-3 9.7 0 13.2M8 1.4c3 3.5 3 9.7 0 13.2" fill="none" stroke="#fff" stroke-width="1.3"/></svg>
        kestreltidesolar.com
      </li>
    </ul>
  </main>
</body>
</html>
```